Dumpling Packaging - Modern/Contemporary and Unique

We need five designs for frozen dumplings and pierogies ( this dumplings/pierogies are Russian/Ukrainian/Belorussian, not to be confused with the Chinese ones as they have very different form and filling and obviously the packaging style is very different) . The product will be sold in USA. The design should be modern, unique, and catch the eye of the consumer. The color for the packaging and main things like logos and small nuances will remain the same on all of them. We want the color of the packaging to be on the darker side. It can be one toned or couple of tones transitioning one into another ( look at examples of packages that are attached). The front of the packaging should have the logo on the top, on the bottom the weight as on the packaging size attachment( it will be the same on all of them), keep frozen sign, and US inspected logo. Under our logo on the top there should be slogan- Crafted for Every Table. Under the slogan there should be the name of the product - Beef Dumplings, Pork Dumplings, Beef and Pork Dumplings, Chicken Dumplings, Potato Pierogies with Bacon. In the left corner there should be a see through window left so that the customer can see the product inside. The size of the opening will depend on the main part that you will use. The main part on the front of the label is that we want a picture of raw meat that the dumplings contain (no ground meats). But it shouldn't be just a picture or drawing, we want it to be made using AI. I've attached three pictures of meat but they are not the one you are to use but just as an example. You can use bigger cuts of meat as long as you can see good quality meat and it looks appealing. Plus some of packages that are attached also have raw meat on the front. So that it looks real but looks better then just real meat. For Beef dumplings the meat should be beef, for chicken dumplings use chicken meat ( you can use both red and white chicken meat), for pork use pork, for beef and pork use beef and pork, for pierogies use potato, bacon, and onion, maybe spices. Don't use meat on bones. No picture of alive animals should be present on the packaging. At the back you need to put nutritional facts and ingredients on one side( they are all attached) and type MANUFACTURED FOR: NORTHPINE KITCHENS 20417 NW 8th CT, Davie, Fl 33318. Also place a small Made in USA logo somewhere in the corner. On the other half of the back you need to put again the name of the dumpling, under cooking instructions ( attached as a word file), under put Safe Handling Instructions, and under place a barcode for specific product ( all five barcodes are attached). I have attached 8 pictures of different dumplings packages that I think slightly resonate with our idea- they have dark colored background, look modern, some have a see through opening of the product. I attached the packaging size as it will go in the print so please follow the sizing standard.

```html
<!DOCTYPE html>
<html lang="en">
<head>
<meta charset="utf-8">
<title>Northpine Kitchens – Dumpling Packaging</title>
<link rel="stylesheet" href="https://fonts.googleapis.com/css2?family=Josefin+Sans:wght@300;400;700&family=Montserrat:wght@700;800&family=Pinyon+Script&display=swap">
<style>
  :root {
    --bg: #e3e5e9;
    --bag-black: #0c0c0d;
    --bag-black-soft: #1b1b1d;
    --gold: #c09a63;
    --gold-light: #dcc7a4;
    --white: #ffffff;
    --beef-red: #d9262b;
    --beef-red-deep: #b51c22;
    --pork-green: #3f9f34;
    --pork-green-deep: #2f8427;
    --window: #dfe1e4;
  }
  html, body {
    margin: 0;
    width: 1200px;
    height: 1200px;
    overflow: hidden;
    background: var(--bg);
  }
  .canvas {
    position: relative;
    width: 1200px;
    height: 1200px;
    background: linear-gradient(180deg, #c9ccd1 0%, var(--bg) 55%, #eceef1 100%);
  }
  .package-row {
    position: absolute;
    top: 380px;
    left: 0;
    width: 1200px;
    display: flex;
    justify-content: center;
    gap: 60px;
  }
  .package {
    width: 480px;
    height: 480px;
    display: block;
  }
  .brand-name {
    font-family: "Josefin Sans", sans-serif;
    font-weight: 700;
    font-size: 27px;
    letter-spacing: 2px;
    fill: var(--gold);
  }
  .slogan {
    font-family: "Josefin Sans", sans-serif;
    font-weight: 300;
    font-size: 15px;
    letter-spacing: 0.5px;
    fill: var(--white);
  }
  .variety {
    font-family: "Montserrat", sans-serif;
    font-weight: 800;
    font-size: 25px;
    letter-spacing: 4px;
    fill: var(--white);
  }
  .product-script {
    font-family: "Pinyon Script", cursive;
    font-size: 46px;
    fill: var(--white);
  }
  .keep-frozen {
    font-family: "Montserrat", sans-serif;
    font-weight: 800;
    font-size: 10.5px;
    fill: var(--white);
  }
  .net-weight {
    font-family: "Josefin Sans", sans-serif;
    font-weight: 400;
    font-size: 5.5px;
    fill: var(--white);
  }
</style>
</head>
<body>
<main class="canvas">
  <div class="package-row">

    <!-- Beef package -->
    <svg class="package package--beef" viewBox="0 0 480 480" xmlns="http://www.w3.org/2000/svg">
      <defs>
        <linearGradient id="beef-body" x1="0" y1="0" x2="1" y2="0">
          <stop offset="0" stop-color="var(--bag-black-soft)"/>
          <stop offset="0.5" stop-color="var(--bag-black)"/>
          <stop offset="1" stop-color="var(--bag-black-soft)"/>
        </linearGradient>
        <linearGradient id="beef-window" x1="0" y1="0" x2="1" y2="0">
          <stop offset="0" stop-color="#f4f5f6"/>
          <stop offset="0.5" stop-color="var(--window)"/>
          <stop offset="1" stop-color="#c8cbcf"/>
        </linearGradient>
        <linearGradient id="beef-meat" x1="0" y1="0" x2="1" y2="1">
          <stop offset="0" stop-color="#d65a5e"/>
          <stop offset="0.55" stop-color="#b8323a"/>
          <stop offset="1" stop-color="#7d1c22"/>
        </linearGradient>
      </defs>
      <rect class="bag-body" x="0" y="0" width="480" height="480" rx="6" fill="url(#beef-body)"/>
      <rect class="top-seal" x="0" y="0" width="480" height="22" fill="#050505"/>
      <path class="colour-band" d="M0,336 C60,332 120,326 170,330 L210,324 C280,320 340,318 400,322 L480,320 L480,480 L0,480 Z" fill="var(--beef-red)"/>
      <rect class="bottom-seal" x="0" y="458" width="480" height="22" fill="var(--beef-red-deep)"/>
      <path class="see-through-window" d="M27,123 C128,126 180,196 177,255 C175,322 120,380 27,384 Z" fill="url(#beef-window)"/>
      <path class="window-trim" d="M27,123 C128,126 180,196 177,255 C175,322 120,380 27,384" fill="none" stroke="var(--gold-light)" stroke-width="5"/>
      <text class="brand-name" x="250" y="78" text-anchor="middle">NORTHPINE KITCHENS</text>
      <text class="slogan" x="250" y="124" text-anchor="middle">Crafted for Every Table</text>
      <g role="img" aria-label="Photograph of two thick raw marbled beef steaks">
        <rect x="207" y="153" width="189" height="198" rx="22" fill="url(#beef-meat)"/>
      </g>
      <line x1="168" y1="381" x2="198" y2="381" stroke="var(--bag-black)" stroke-width="2"/>
      <line x1="283" y1="381" x2="313" y2="381" stroke="var(--bag-black)" stroke-width="2"/>
      <text class="variety" x="241" y="390" text-anchor="middle">BEEF</text>
      <text class="product-script" x="240" y="430" text-anchor="middle">Dumplings</text>
      <circle class="inspection-badge" cx="393" cy="384" r="19" fill="none" stroke="var(--white)" stroke-width="1"/>
      <circle class="frozen-icon" cx="368" cy="419" r="10" fill="none" stroke="var(--white)" stroke-width="2"/>
      <path d="M368,412 V426 M361,419 H375 M363,414 L373,424 M373,414 L363,424" stroke="var(--white)" stroke-width="1.2"/>
      <text class="keep-frozen" x="381" y="417">KEEP</text>
      <text class="keep-frozen" x="381" y="428">FROZEN</text>
      <text class="net-weight" x="361" y="441">NET WT. 32 OZ. (2 LB) 907g</text>
    </svg>

    <!-- Pork package -->
    <svg class="package package--pork" viewBox="0 0 480 480" xmlns="http://www.w3.org/2000/svg">
      <defs>
        <linearGradient id="pork-body" x1="0" y1="0" x2="1" y2="0">
          <stop offset="0" stop-color="var(--bag-black-soft)"/>
          <stop offset="0.5" stop-color="var(--bag-black)"/>
          <stop offset="1" stop-color="var(--bag-black-soft)"/>
        </linearGradient>
        <linearGradient id="pork-window" x1="0" y1="0" x2="1" y2="0">
          <stop offset="0" stop-color="#f4f5f6"/>
          <stop offset="0.5" stop-color="var(--window)"/>
          <stop offset="1" stop-color="#c8cbcf"/>
        </linearGradient>
        <linearGradient id="pork-meat" x1="0" y1="0" x2="1" y2="1">
          <stop offset="0" stop-color="#f6c2b6"/>
          <stop offset="0.6" stop-color="#eba898"/>
          <stop offset="1" stop-color="#d98c7d"/>
        </linearGradient>
      </defs>
      <rect class="bag-body" x="0" y="0" width="480" height="480" rx="6" fill="url(#pork-body)"/>
      <rect class="top-seal" x="0" y="0" width="480" height="22" fill="#050505"/>
      <path class="colour-band" d="M0,336 C60,332 120,326 170,330 L210,324 C280,320 340,318 400,322 L480,320 L480,480 L0,480 Z" fill="var(--pork-green)"/>
      <rect class="bottom-seal" x="0" y="458" width="480" height="22" fill="var(--pork-green-deep)"/>
      <path class="see-through-window" d="M27,123 C128,126 180,196 177,255 C175,322 120,380 27,384 Z" fill="url(#pork-window)"/>
      <path class="window-trim" d="M27,123 C128,126 180,196 177,255 C175,322 120,380 27,384" fill="none" stroke="var(--gold-light)" stroke-width="5"/>
      <text class="brand-name" x="250" y="78" text-anchor="middle">NORTHPINE KITCHENS</text>
      <text class="slogan" x="250" y="128" text-anchor="middle">Crafted for Every Table</text>
      <g role="img" aria-label="Photograph of a thick raw pork loin cut">
        <rect x="207" y="182" width="218" height="170" rx="16" fill="url(#pork-meat)"/>
      </g>
      <line x1="163" y1="381" x2="193" y2="381" stroke="var(--bag-black)" stroke-width="2"/>
      <line x1="289" y1="381" x2="319" y2="381" stroke="var(--bag-black)" stroke-width="2"/>
      <text class="variety" x="242" y="390" text-anchor="middle">PORK</text>
      <text class="product-script" x="240" y="430" text-anchor="middle">Dumplings</text>
      <circle class="inspection-badge" cx="393" cy="384" r="19" fill="none" stroke="var(--white)" stroke-width="1"/>
      <circle class="frozen-icon" cx="368" cy="419" r="10" fill="none" stroke="var(--white)" stroke-width="2"/>
      <path d="M368,412 V426 M361,419 H375 M363,414 L373,424 M373,414 L363,424" stroke="var(--white)" stroke-width="1.2"/>
      <text class="keep-frozen" x="381" y="417">KEEP</text>
      <text class="keep-frozen" x="381" y="428">FROZEN</text>
      <text class="net-weight" x="361" y="441">NET WT. 32 OZ. (2 LB) 907g</text>
    </svg>

  </div>
</main>
</body>
</html>
```